Velmora Business Card

We need a design for business cards for our new company. We are a resident safety and security company company that focuses on senior living communities. we provide Nurse call, Access control, CCTV, Wired and wireless network infrastructure, Wander Management, and much more!

Our logo is the circuit board shield. Representing our high tech security solutions. I would like the business card to bring the same theme with perhaps some circuit board traces around the card similar to our logo

```html
<!DOCTYPE html>
<html lang="en">
<head>
<meta charset="utf-8">
<title>Velmora Business Card</title>
<link href="https://fonts.googleapis.com/css2?family=Tinos:wght@400;700&family=Arimo:wght@400&display=swap" rel="stylesheet">
<style>
  :root {
    --backdrop: #e4e4e4;
    --card: #ffffff;
    --blue-deep: #0656cc;
    --blue-mid: #0a86e0;
    --blue-light: #0aa8ec;
    --ink: #444444;
    --ink-dark: #333333;
  }
  * { margin: 0; padding: 0; box-sizing: border-box; }
  html, body { width: 1200px; height: 1200px; overflow: hidden; background: var(--backdrop); }
  .canvas { position: relative; width: 1200px; height: 1200px; }
  .card {
    position: absolute; width: 688px; height: 393px; background: var(--card);
    border-radius: 22px; overflow: hidden;
  }
  .card--front { left: 267px; top: 158px; }
  .card--back { left: 263px; top: 653px; }
  .card__shapes { position: absolute; inset: 0; width: 100%; height: 100%; }

  .brand-name {
    position: absolute; font-family: "Tinos", serif; font-weight: 400;
    letter-spacing: 1px; white-space: nowrap; transform: translateX(-50%);
  }
  .brand-mark { position: absolute; border-radius: 50%; transform: translateX(-50%); }
  .card--front .brand-name { left: 546px; top: 166px; font-size: 34px; color: #ffffff; }
  .card--front .brand-mark { left: 546px; top: 52px; width: 104px; height: 104px; background: rgba(255,255,255,0.22); }
  .card--back .brand-name { left: 360px; top: 244px; font-size: 48px; color: var(--blue-deep); }
  .card--back .brand-mark { left: 354px; top: 92px; width: 140px; height: 140px; background: linear-gradient(180deg, var(--blue-light), var(--blue-deep)); }

  .contact-list { position: absolute; left: 37px; top: 160px; list-style: none; }
  .contact-list__item {
    display: flex; align-items: center; height: 33.5px;
    font-family: "Arimo", sans-serif; font-size: 16px; color: var(--ink);
  }
  .contact-list__icon { width: 25px; height: 25px; margin-right: 12px; flex: none; }

  .holder { position: absolute; left: 39px; top: 311px; }
  .holder__name {
    font-family: "Tinos", serif; font-weight: 700; font-size: 28px;
    letter-spacing: 1px; color: var(--blue-deep); line-height: 1;
  }
  .holder__role {
    font-family: "Arimo", sans-serif; font-size: 15px; color: var(--ink-dark);
    margin-left: -3px; margin-top: 4px;
  }
</style>
</head>
<body>
<div class="canvas">

  <section class="card card--front">
    <svg class="card__shapes" viewBox="0 0 688 393" aria-hidden="true">
      <defs>
        <radialGradient id="frontSweep" cx="0.55" cy="0.3" r="0.7">
          <stop offset="0" stop-color="#0aa8ec"/>
          <stop offset="0.6" stop-color="#0a86e0"/>
          <stop offset="1" stop-color="#0656cc"/>
        </radialGradient>
        <radialGradient id="frontGlow" cx="0.5" cy="0.4" r="0.6">
          <stop offset="0" stop-color="#0ab0f0"/>
          <stop offset="1" stop-color="#0568d6"/>
        </radialGradient>
      </defs>
      <path d="M101,0 C190,170 380,330 688,318 L688,0 Z" fill="url(#frontSweep)"/>
      <path d="M101,0 C150,90 230,180 300,180 C420,182 590,100 640,0 Z" fill="url(#frontGlow)" opacity="0.6"/>
    </svg>
    <span class="brand-mark"></span>
    <span class="brand-name">Velmora</span>

    <ul class="contact-list">
      <li class="contact-list__item">
        <svg class="contact-list__icon" viewBox="0 0 24 24"><circle cx="12" cy="12" r="12" fill="#0656cc"/><path d="M8.2 6.5l2 2.4-1.2 1.4c.8 1.7 2 2.9 3.7 3.7l1.4-1.2 2.4 2-1.1 1.8c-4.2-.4-8.5-4.7-8.9-8.9z" fill="#fff"/></svg>
        (555) 214-7730
      </li>
      <li class="contact-list__item">
        <svg class="contact-list__icon" viewBox="0 0 24 24"><circle cx="12" cy="12" r="12" fill="#0656cc"/><rect x="8.5" y="5.5" width="7" height="13" rx="1.3" fill="#fff"/><rect x="9.7" y="7.2" width="4.6" height="8.6" fill="#0a86e0"/></svg>
        (555) 381-4462
      </li>
      <li class="contact-list__item">
        <svg class="contact-list__icon" viewBox="0 0 24 24"><circle cx="12" cy="12" r="12" fill="#0656cc"/><rect x="6.5" y="8" width="11" height="8" rx="0.8" fill="#fff"/><path d="M6.8 8.4l5.2 4 5.2-4" stroke="#0656cc" stroke-width="1" fill="none"/></svg>
        Owen@Velmora.com
      </li>
      <li class="contact-list__item">
        <svg class="contact-list__icon" viewBox="0 0 24 24"><circle cx="12" cy="12" r="12" fill="#0656cc"/><circle cx="12" cy="12" r="6" fill="#fff"/><path d="M9 9.5c1.5-.5 2.5.5 2 1.8-.6 1.3.6 2.4 1.6 3.5M13.5 7c.3 1 1.6 1.2 2.3 2" stroke="#0a86e0" stroke-width="1.3" fill="none"/></svg>
        www.Velmora.com
      </li>
    </ul>

    <div class="holder">
      <p class="holder__name">OWEN MARLOWE</p>
      <p class="holder__role">President</p>
    </div>
  </section>

  <section class="card card--back">
    <svg class="card__shapes" viewBox="0 0 688 393" aria-hidden="true">
      <defs>
        <radialGradient id="backTop" cx="0.5" cy="0.2" r="0.8">
          <stop offset="0" stop-color="#0aa8ec"/>
          <stop offset="1" stop-color="#0656cc"/>
        </radialGradient>
        <radialGradient id="backBottom" cx="0.5" cy="0.7" r="0.8">
          <stop offset="0" stop-color="#0aa8ec"/>
          <stop offset="1" stop-color="#0656cc"/>
        </radialGradient>
      </defs>
      <path d="M438,0 C480,80 580,126 688,126 L688,0 Z" fill="url(#backTop)"/>
      <path d="M0,265 C100,255 200,300 248,393 L0,393 Z" fill="url(#backBottom)"/>
    </svg>
    <span class="brand-mark"></span>
    <span class="brand-name">Velmora</span>
  </section>

</div>
</body>
</html>
```